Delmer's Pressure Washing Services

Starting a pressure washing business on my own in Central Valley California, not too much experience so affordable, I do houses, fences, driveways, cars, trailers, RVs. Planning to make this full-time hoping clientele picks up after having a nice business card. Design doesn't have to be flashy, more to the point, I like simplistic/personable. I do not want something exhausting to look at or with too much going on.

Target Market(s)

Residential, Commercial

Industry/Entity Type

Pressure Washing

Contact Information for Business Card

avalible Services

Font styles to use
Sans Serif

Colors
0054AA
0677BA
7BADD7
CADEEF
E8F1F8
0094D4
00A9DD
6FCCEA
C7EBF8
E9F6FB
00AB8E
00BBA5
67D7C9
C6EFE9
E9F9F6

```html
<!DOCTYPE html>
<html lang="en">
<head>
<meta charset="utf-8">
<title>Delmer's Pressure Washing Services – Business Card</title>
<link rel="stylesheet" href="https://fonts.googleapis.com/css2?family=Questrial&display=swap">
<style>
  :root {
    --blue-deep: #0054AA;
    --blue-mid: #0677BA;
    --blue-soft: #7BADD7;
    --blue-pale: #CADEEF;
    --ink: #1d1d1f;
    --ink-soft: #6b7280;
    --paper: #ffffff;
    --backdrop: #eef1f4;
  }
  * { box-sizing: border-box; margin: 0; padding: 0; }
  html, body {
    width: 1200px; height: 786px; overflow: hidden;
    background: var(--backdrop);
    font-family: "Questrial", "Century Gothic", sans-serif;
  }
  .canvas {
    width: 1200px; height: 786px;
    display: flex; align-items: center; justify-content: center;
  }
  .business-card {
    position: relative;
    width: 1000px; height: 572px;
    background: var(--paper);
    box-shadow: 0 10px 30px rgba(0, 40, 90, 0.12);
  }
  .brand {
    position: absolute; top: 120px; left: 0; right: 0;
    display: flex; flex-direction: column; align-items: center;
    color: var(--blue-mid);
    text-transform: uppercase;
  }
  .brand-mark {
    width: 34px; height: 34px; border-radius: 50%;
    background: var(--blue-mid);
    margin-bottom: 22px;
  }
  .brand-name {
    font-size: 38px; letter-spacing: 3px; line-height: 1.3;
    text-align: center;
  }
  .divider {
    position: absolute; top: 286px; left: 50px; right: 50px;
    height: 1.5px; background: var(--blue-soft);
  }
  .owner {
    position: absolute; top: 358px; left: 60px; width: 390px;
    text-align: right;
  }
  .owner-name {
    color: var(--blue-deep);
    font-size: 44px; letter-spacing: 3px; text-transform: uppercase; line-height: 1;
  }
  .owner-title {
    color: var(--ink); font-size: 25px; margin-top: 6px;
  }
  .column-rule {
    position: absolute; top: 345px; left: 474px;
    width: 2px; height: 90px; background: var(--blue-deep);
  }
  .contact-list {
    position: absolute; top: 344px; left: 500px;
    list-style: none;
  }
  .contact-item {
    display: flex; align-items: center; gap: 12px;
    color: var(--ink); font-size: 27px; line-height: 33px;
  }
  .contact-icon { width: 20px; height: 20px; flex: none; }
  .address {
    position: absolute; top: 494px; left: 0; right: 0;
    text-align: center; color: var(--ink); font-size: 25px;
  }
</style>
</head>
<body>
  <main class="canvas">
    <article class="business-card">
      <header class="brand">
        <span class="brand-mark" aria-hidden="true"></span>
        <h1 class="brand-name">Delmer's<br>Pressure Washing Services</h1>
      </header>

      <div class="divider"></div>

      <section class="owner">
        <p class="owner-name">Delmer Ruiz</p>
        <p class="owner-title">Owner</p>
      </section>

      <div class="column-rule"></div>

      <ul class="contact-list">
        <li class="contact-item">
          <svg class="contact-icon" viewBox="0 0 24 24" aria-hidden="true">
            <path fill="none" stroke="#6b7280" stroke-width="2" d="M6 3h3l2 5-2.5 1.5a12 12 0 0 0 6 6L16 13l5 2v3a3 3 0 0 1-3 3A16 16 0 0 1 3 6a3 3 0 0 1 3-3z"/>
          </svg>
          209 555 0148
        </li>
        <li class="contact-item">
          <svg class="contact-icon" viewBox="0 0 24 24" aria-hidden="true">
            <rect x="2" y="5" width="20" height="14" fill="#6b7280"/>
            <path d="M2 5l10 8 10-8" fill="none" stroke="#fff" stroke-width="1.8"/>
          </svg>
          delmer@delmerswash.com
        </li>
        <li class="contact-item">
          <svg class="contact-icon" viewBox="0 0 24 24" aria-hidden="true">
            <g fill="none" stroke="#6b7280" stroke-width="1.8">
              <circle cx="12" cy="12" r="9.5"/>
              <ellipse cx="12" cy="12" rx="4.5" ry="9.5"/>
              <path d="M2.5 12h19M4.5 7h15M4.5 17h15"/>
            </g>
          </svg>
          www.delmerswash.com
        </li>
      </ul>

      <p class="address">00 Orchard Bend Road, Modesto, CA 00000</p>
    </article>
  </main>
</body>
</html>
```